Construction business card

I need a new business card, they can connect with my logo, brand.
What we do is residential house , design and build
I like: Navy blue / black
I attached our logo, brand,
and, some idea for business card.

```html
<!DOCTYPE html>
<html lang="en">
<head>
<meta charset="utf-8">
<title>Halden Building Group – Business Card</title>
<link rel="stylesheet" href="https://fonts.googleapis.com/css2?family=Montserrat:wght@500;600;700;800&display=swap">
<style>
  :root {
    --page-bg: #e6e6e3;
    --card-dark: #3a3f47;
    --card-light: #f6f5f1;
    --brand-blue: #1f5a96;
    --ink: #23272d;
    --ink-soft: #4a4f57;
    --rule: #8a8e94;
    --white: #ffffff;
  }
  * { box-sizing: border-box; margin: 0; padding: 0; }
  html, body {
    width: 1200px; height: 1200px; overflow: hidden;
    background: var(--page-bg);
    font-family: "Montserrat", Arial, sans-serif;
  }
  .sheet {
    width: 1200px; height: 1200px;
    display: flex; flex-direction: column; align-items: center; justify-content: center;
    gap: 60px;
  }
  .card {
    width: 900px; height: 514px;
    border-radius: 34px;
    position: relative; overflow: hidden;
    box-shadow: 0 10px 30px rgba(0,0,0,0.12);
  }

  /* Back side */
  .card--back {
    background: var(--card-dark);
    display: flex; align-items: center; justify-content: center;
  }
  .brand-mark {
    display: flex; align-items: center; gap: 22px;
  }
  .brand-mark__square {
    width: 34px; height: 34px; background: var(--white);
  }
  .brand-mark__name {
    color: var(--white);
    font-weight: 800; font-size: 48px; letter-spacing: 1px;
    text-transform: uppercase; line-height: 1;
  }

  /* Front side */
  .card--front { background: var(--card-light); }
  .front__logo {
    position: absolute; left: 56px; top: 150px; width: 330px;
    display: flex; align-items: center; gap: 16px;
  }
  .front__logo .brand-mark__square { width: 26px; height: 26px; background: var(--brand-blue); flex: none; }
  .front__logo .brand-mark__name { color: var(--brand-blue); font-size: 34px; line-height: 1.15; }

  .front__details { position: absolute; left: 430px; top: 56px; right: 56px; }
  .person__name {
    font-weight: 700; font-size: 40px; color: var(--ink);
    text-transform: uppercase; letter-spacing: 1px; line-height: 1.1;
  }
  .person__title { font-weight: 500; font-size: 20px; color: var(--ink-soft); margin-top: 4px; }
  .details__rule { height: 2px; background: var(--rule); margin: 18px 0 22px; }
  .contact-list { list-style: none; display: flex; flex-direction: column; gap: 14px; }
  .contact-list li {
    display: flex; align-items: center; gap: 16px;
    font-size: 18px; font-weight: 500; color: var(--ink-soft);
  }
  .contact-list svg { width: 20px; height: 20px; flex: none; fill: none; stroke: var(--ink); stroke-width: 2; stroke-linecap: round; stroke-linejoin: round; }

  .tagline-band {
    position: absolute; left: 0; right: 0; bottom: 0; height: 72px;
    background: var(--brand-blue);
    display: flex; align-items: center; padding-left: 56px;
    color: var(--white); font-weight: 700; font-size: 24px;
    text-transform: uppercase; letter-spacing: 1.5px;
  }
</style>
</head>
<body>
<main class="sheet">
  <section class="card card--back" aria-label="Card back">
    <div class="brand-mark">
      <span class="brand-mark__square"></span>
      <span class="brand-mark__name">Halden Building Group</span>
    </div>
  </section>

  <section class="card card--front" aria-label="Card front">
    <div class="front__logo brand-mark">
      <span class="brand-mark__square"></span>
      <span class="brand-mark__name">Halden Building Group</span>
    </div>

    <div class="front__details">
      <h1 class="person__name">Jordan Vale</h1>
      <p class="person__title">Managing Director</p>
      <div class="details__rule"></div>
      <ul class="contact-list">
        <li>
          <svg viewBox="0 0 24 24"><path d="M5 3h4l2 5-2.5 1.5a11 11 0 0 0 6 6L16 13l5 2v4a2 2 0 0 1-2 2A17 17 0 0 1 3 5a2 2 0 0 1 2-2z"/></svg>
          (555) 284-9102
        </li>
        <li>
          <svg viewBox="0 0 24 24"><rect x="3" y="5" width="18" height="14" rx="1"/><path d="M3 6l9 7 9-7"/></svg>
          jordan.vale@haldenbuild.com
        </li>
        <li>
          <svg viewBox="0 0 24 24"><circle cx="12" cy="12" r="9"/><path d="M3 12h18M12 3c3 3 3 15 0 18M12 3c-3 3-3 15 0 18"/></svg>
          www.haldenbuild.com
        </li>
        <li>
          <svg viewBox="0 0 24 24"><path d="M12 21s-7-6.5-7-12a7 7 0 0 1 14 0c0 5.5-7 12-7 12z"/><circle cx="12" cy="9" r="2.5"/></svg>
          48 Timber Row, Oakmont, CA
        </li>
      </ul>
    </div>

    <div class="tagline-band">Quality Construction. Timeless Design.</div>
  </section>
</main>
</body>
</html>
```